Business Card Design - Photographer

I am a landscape photographer and I require a business card design. 

I require two designs:
1)  a double sided business card
 and
b)  a single sided business card 

The single sided design can either be the same as the double sided (with just one side having all the information)....or it can be an entire new design. Its up to you.

My corporate colours are (CMYK):

Blue   69, 32, 0, 0
Grey  72,  64,  47,  31
Green  32,  2,  91,  0
Yellow   0, 19, 92, 0
Orange  0, 39, 75, 0

Colour space in final file should be in CMYK.

The details that need to be included on the card:

- Use the provided Logo
- Name: Lukas Wendrovski
- Email:   sales@vistaplume.com.au
- Website:    vistaplume.com.au
- Kestrel:    kestrel.net/vistaplume
- Folkwall:   folkwall.com/vistaplume
- Mobile  0491 570 156

Please use the attached template to design the logo to the specified size, including the marked bleed lines. I have also attached my logo in PNG (transparent background) and ai format for you to use.

The final file should be:
- Photoshop version with layers so I can edit the name/text etc. All non vector files should be high resolution at 1039 x 697 pixels at 300 dpi.

I also require a file as:
- Vector based PDF

Anyway questions please contact me.

Thank you

Industry/Entity Type

Landscape

Logo styles of interest
Pictorial/Combination Logo
Abstract Logo
Wordmark Logo
Lettermark Logo
Requirements
Must have
• The details that need to be included on the card:

- Use the provided Logo
- Name: Lukas Wendrovski
- Email: sales@vistaplume.com.au
- Website: vistaplume.com.au
- Kestrel: kestrel.net/vistaplume
- Folkwall: folkwall.com/vistaplume
- Mobile 0491 570 156

```html
<!DOCTYPE html>
<html lang="en">
<head>
<meta charset="utf-8">
<title>Vistaplume – Business Card</title>
<link rel="stylesheet" href="https://fonts.googleapis.com/css2?family=Cinzel:wght@400;600;900&display=swap">
<style>
  :root {
    --bleed-grey: #c8c9cb;
    --paper: #ffffff;
    --ink: #3c3f4f;
    --frame-green: #9cc93d;
    --trim-line: #1e1e1e;
  }
  html, body {
    margin: 0;
    padding: 0;
    width: 1200px;
    height: 805px;
    overflow: hidden;
    background: var(--bleed-grey);
  }
  .card {
    position: relative;
    width: 1200px;
    height: 805px;
    background: var(--bleed-grey);
    font-family: "Cinzel", serif;
    color: var(--ink);
  }
  .card__trim {
    position: absolute;
    left: 29px; top: 29px;
    width: 1143px; height: 747px;
    box-sizing: border-box;
    background: var(--paper);
    border: 2px dashed var(--trim-line);
  }
  .card__frame {
    position: absolute;
    left: 55px; top: 55px;
    width: 1090px; height: 696px;
    box-sizing: border-box;
    border: 4px solid var(--frame-green);
  }
  .brand__mark {
    position: absolute;
    left: 485px; top: 81px;
  }
  .brand__name {
    position: absolute;
    left: 294px; top: 335px;
    width: 613px;
    margin: 0;
    font-size: 58px;
    font-weight: 600;
    letter-spacing: 4px;
    line-height: 58px;
    text-align: center;
    white-space: nowrap;
  }
  .brand__rule {
    position: absolute;
    left: 294px; top: 401px;
    width: 613px; height: 2px;
    background: var(--ink);
  }
  .brand__tagline {
    position: absolute;
    left: 294px; top: 414px;
    width: 613px;
    margin: 0;
    font-size: 21px;
    font-weight: 600;
    letter-spacing: 5px;
    line-height: 24px;
    text-align: center;
    white-space: nowrap;
  }
  .contact {
    position: absolute;
    left: 150px;
    top: 476px;
    width: 907px;
    margin: 0;
  }
  .contact__row {
    display: flex;
    justify-content: space-between;
    align-items: baseline;
    height: 40px;
    line-height: 40px;
  }
  .contact__label {
    font-size: 30px;
    font-weight: 600;
    margin: 0;
  }
  .contact__value {
    font-size: 25px;
    font-weight: 400;
    margin: 0;
    text-transform: lowercase;
    white-space: nowrap;
  }
  .contact__value--name {
    font-weight: 900;
    font-size: 30px;
    text-transform: none;
  }
  .contact__value--phone {
    font-size: 26px;
  }
</style>
</head>
<body>
  <main class="card">
    <div class="card__trim"></div>
    <div class="card__frame"></div>

    <svg class="brand__mark" width="230" height="230" viewBox="0 0 230 230" aria-hidden="true">
      <circle cx="115" cy="115" r="114" fill="var(--ink)"/>
    </svg>
    <h1 class="brand__name">VISTAPLUME</h1>
    <div class="brand__rule"></div>
    <p class="brand__tagline">FINE ART PHOTOGRAPHY</p>

    <dl class="contact">
      <div class="contact__row">
        <dt class="contact__label">Name</dt>
        <dd class="contact__value contact__value--name">Lukas Wendrovski</dd>
      </div>
      <div class="contact__row">
        <dt class="contact__label">Email</dt>
        <dd class="contact__value">sales@vistaplume.com.au</dd>
      </div>
      <div class="contact__row">
        <dt class="contact__label">Website</dt>
        <dd class="contact__value">vistaplume.com.au</dd>
      </div>
      <div class="contact__row">
        <dt class="contact__label">Kestrel</dt>
        <dd class="contact__value">kestrel.net/vistaplume</dd>
      </div>
      <div class="contact__row">
        <dt class="contact__label">Folkwall</dt>
        <dd class="contact__value">folkwall.com/vistaplume</dd>
      </div>
      <div class="contact__row">
        <dt class="contact__label">Mobile</dt>
        <dd class="contact__value contact__value--phone">0491 570 156</dd>
      </div>
    </dl>
  </main>
</body>
</html>
```